Business card design needed

Need a new business card design for a new business in Sydney, Australia called 'Verrowin Australia'. The business deals in consulting for new sales, sales leadership and customer service consultancy. Want the business card to look professional and clean

Industry/Entity Type

Leadership

Contact Information for Business Card

Verrowin Australia
Tobias Wrenley
Managing Director

14 Quarrion Avenue
Marrowdale NSW 2041

0432 517 806
tobias@verrowin.com.au
www.verrowin.com.au

```html
<!DOCTYPE html>
<html lang="en">
<head>
<meta charset="utf-8">
<title>Verrowin Australia – Business Card</title>
<link href="https://fonts.googleapis.com/css2?family=Questrial&display=swap" rel="stylesheet">
<style>
  :root {
    --page: #e9e6e1;
    --card-front: #141414;
    --card-front-stripe: #1d1d1d;
    --card-back: #2b2b2b;
    --green: #8dc63f;
    --green-deep: #6fa52b;
    --text-light: #d9d9d9;
    --text-grey: #9a9a9a;
    --icon-box: #1a1a1a;
  }
  * { box-sizing: border-box; margin: 0; padding: 0; }
  html, body { width: 1200px; height: 733px; overflow: hidden; background: var(--page); }
  body { font-family: "Questrial", "Century Gothic", sans-serif; position: relative; }

  .card {
    position: absolute;
    top: 206px;
    width: 540px;
    height: 320px;
    border-radius: 16px;
    overflow: hidden;
    box-shadow: 0 10px 28px rgba(0,0,0,.25);
  }

  /* Front side */
  .card--front {
    left: 50px;
    background:
      radial-gradient(ellipse at 45% 40%, rgba(255,255,255,.07), transparent 65%),
      repeating-linear-gradient(90deg, var(--card-front) 0 14px, var(--card-front-stripe) 14px 28px);
  }
  .front-brand {
    position: absolute;
    left: 60px;
    top: 108px;
    font-size: 46px;
    letter-spacing: -0.5px;
    color: var(--green);
    white-space: nowrap;
  }
  .services { list-style: none; position: absolute; left: 0; top: 0; width: 100%; }
  .service {
    position: absolute;
    display: flex;
    align-items: center;
    gap: 7px;
    font-size: 12px;
    white-space: nowrap;
  }
  .service::before {
    content: "";
    width: 6px; height: 6px; border-radius: 50%;
    background: currentColor;
  }
  .service--green { color: var(--green); }
  .service--white { color: var(--text-light); }
  .service:nth-child(1) { left: 66px;  top: 166px; }
  .service:nth-child(2) { left: 152px; top: 184px; }
  .service:nth-child(3) { left: 250px; top: 204px; }

  /* Back side */
  .card--back { left: 610px; background: var(--card-back); }
  .back-brand {
    position: absolute;
    left: 30px;
    top: 50px;
    font-size: 30px;
    letter-spacing: -0.3px;
    color: var(--green);
    white-space: nowrap;
  }
  .contact-band {
    position: absolute;
    left: 262px;
    right: 0;
    top: 92px;
    height: 96px;
    background: linear-gradient(180deg, var(--green), var(--green-deep));
    padding: 12px 0 0 14px;
    display: flex;
    flex-direction: column;
    gap: 8px;
  }
  .contact-row {
    display: flex;
    align-items: center;
    gap: 8px;
    font-size: 10.5px;
    color: var(--icon-box);
    white-space: nowrap;
  }
  .contact-icon {
    width: 18px; height: 18px;
    background: var(--icon-box);
    border-radius: 3px;
    display: flex; align-items: center; justify-content: center;
    flex: none;
  }
  .contact-icon svg { width: 12px; height: 12px; fill: var(--green); }
  .person { position: absolute; left: 70px; top: 196px; }
  .person-name { font-size: 21px; color: var(--green); }
  .person-role { font-size: 12px; color: var(--text-grey); margin-top: 2px; }
  .website {
    position: absolute;
    left: 276px;
    top: 200px;
    font-size: 10.5px;
    color: var(--text-grey);
  }
</style>
</head>
<body>

<section class="card card--front" aria-label="Card front">
  <div class="front-brand">Verrowin Australia</div>
  <ul class="services">
    <li class="service service--green">consulting for new sales</li>
    <li class="service service--white">sales leadership</li>
    <li class="service service--green">customer service consultancy</li>
  </ul>
</section>

<section class="card card--back" aria-label="Card back">
  <div class="back-brand">Verrowin Australia</div>

  <div class="contact-band">
    <div class="contact-row">
      <span class="contact-icon">
        <svg viewBox="0 0 24 24"><path d="M6.6 10.8a15.1 15.1 0 0 0 6.6 6.6l2.2-2.2c.3-.3.7-.4 1-.2 1.1.4 2.3.6 3.6.6.6 0 1 .4 1 1V20c0 .6-.4 1-1 1C10.6 21 3 13.4 3 4c0-.6.4-1 1-1h3.5c.6 0 1 .4 1 1 0 1.3.2 2.5.6 3.6.1.3 0 .7-.2 1z"/></svg>
      </span>
      0432 517 806
    </div>
    <div class="contact-row">
      <span class="contact-icon">
        <svg viewBox="0 0 24 24"><path d="M3 5h18v14H3zm2 2v.5l7 4.5 7-4.5V7l-7 4.5z"/></svg>
      </span>
      tobias@verrowin.com.au
    </div>
    <div class="contact-row">
      <span class="contact-icon">
        <svg viewBox="0 0 24 24"><path d="M12 2a7 7 0 0 0-7 7c0 5.2 7 13 7 13s7-7.8 7-13a7 7 0 0 0-7-7zm0 9.5a2.5 2.5 0 1 1 0-5 2.5 2.5 0 0 1 0 5z"/></svg>
      </span>
      14 Quarrion Avenue Marrowdale NSW 2041
    </div>
  </div>

  <div class="person">
    <div class="person-name">Tobias Wrenley</div>
    <div class="person-role">Managing Director</div>
  </div>

  <div class="website">www.verrowin.com.au</div>
</section>

</body>
</html>
```